Mission Vision and Values Infographic

We are a healthcare organisation and would like to create a graphic which showcases our Mission, Vision and Values in a clear and beautiful manner.

Attached is:

* Our mission vision and values.
* Style Guide
* Examples of other designs found on the web
* Logo

Your design should be Simple, Clear, Professional and Beautiful.

If you prefer, you can submit a Basic design to start off with for initial feedback before then refining in a future submission. Please check back in the comments section as I will be providing additional general remarks if needed.

The design needs to be created in a tool which will then allow us to modify it in the future…. Ideally either Adobe InDesign, Adobe Illustrator or Adobe Photoshop. Vector is preferred.

All together, the whole design needs to be:

* Printable on one sheet of A3 size paper (to go on our wall)
* Be able to go on a webpage

So there might be slight variations for bigger and smaller displays. For example, the A3 Page will have all three - Mission, Vision and Values + Logo together. The version for a webpage might be separated into 3 parts to make it easier to show on a webpage.

Good luck and happy designing

```html
<!DOCTYPE html>
<html lang="en">
<head>
<meta charset="utf-8">
<title>Vision, Mission and Values</title>
<link href="https://fonts.googleapis.com/css2?family=Open+Sans:wght@700&family=Arimo:wght@400;700&family=Roboto:wght@400&display=swap" rel="stylesheet">
<style>
  :root {
    --navy: #0f4a8c;
    --sky: #29a8e0;
    --canvas: #e9e9ef;
    --white: #ffffff;
    --ink: #222428;
    --red: #ec1c2a;
    --cyan: #6ccbdc;
    --green: #6cbd45;
    --purple: #b24f9f;
    --yellow: #e9dc12;
    --blue: #3a4fa3;
  }
  * { margin: 0; padding: 0; box-sizing: border-box; }
  html, body { width: 848px; height: 1200px; overflow: hidden; background: var(--canvas); }
  .sheet { position: relative; width: 848px; height: 1200px; background: var(--canvas); font-family: "Arimo", Arial, sans-serif; }
  .statement { position: absolute; left: 0; width: 848px; text-align: center; color: var(--white); }
  .statement--vision { top: 0; height: 178px; background: var(--navy); }
  .statement--mission { top: 178px; height: 175px; background: var(--sky); }
  .statement__title { font-family: "Open Sans", Arial, sans-serif; font-weight: 700; font-size: 25px; line-height: 1; padding-top: 20px; }
  .statement__text { font-size: 18.5px; line-height: 24px; margin-top: 12px; }
  .statement--mission .statement__text { margin-top: 14px; }
  .wheel { position: absolute; left: 0; top: 0; width: 848px; height: 1200px; }
  .segment { filter: drop-shadow(0 4px 6px rgba(0,0,0,0.16)); }
  .value { position: absolute; width: 240px; text-align: center; }
  .value__title { font-family: "Arimo", Arial, sans-serif; font-weight: 700; font-size: 27px; line-height: 30px; }
  .value__text { font-family: "Roboto", Arial, sans-serif; font-size: 10.4px; line-height: 19px; color: var(--ink); margin-top: 9px; }
  .value--quality { left: 199px; top: 482px; }
  .value--quality .value__title { color: var(--red); }
  .value--flexibility { left: 418px; top: 482px; }
  .value--flexibility .value__title { color: var(--cyan); }
  .value--flexibility .value__text { margin-left: 12px; }
  .value--diversity { left: 90px; top: 657px; }
  .value--diversity .value__title { color: var(--blue); }
  .value--positivity { left: 533px; top: 657px; }
  .value--positivity .value__title { color: var(--green); }
  .value--creativity { left: 195px; top: 869px; }
  .value--creativity .value__title { color: var(--yellow); }
  .value--creativity .value__text { margin-top: 2px; }
  .value--integrity { left: 429px; top: 869px; }
  .value--integrity .value__title { color: var(--purple); }
  .value--integrity .value__text { margin-top: 0; }
</style>
</head>
<body>
<main class="sheet">
  <section class="statement statement--vision">
    <h1 class="statement__title">Our Vision</h1>
    <p class="statement__text">Individuals of all abilities will have the opportunity to achieve their therapy<br>goals by accessing gold standard services, so they may confidently<br>participate in the wider community where they will be understood,<br>supported and embraced for their individuality</p>
  </section>
  <section class="statement statement--mission">
    <h2 class="statement__title">Our Mission</h2>
    <p class="statement__text">At Harbourside Speech Clinic we strive to ensure our clients and families have<br>access to high quality, evidence-based intervention from a passionate and<br>professional team to improve and develop individual functional skills that<br>contribute to successful participation in the community</p>
  </section>

  <svg class="wheel" viewBox="0 0 848 1200" aria-hidden="true">
    <defs>
      <path id="segment-shape" d="M0,-30 L0,-300 Q0,-330 30,-328.6 A330 330 0 0 1 271,-188 Q286,-165 260,-150 L26,-15 Q0,0 0,-30 Z"/>
      <clipPath id="segment-clip"><use href="#segment-shape"/></clipPath>
    </defs>

    <g transform="translate(432 738) rotate(-60)"><g class="segment" transform="translate(5 -8.5)"><g clip-path="url(#segment-clip)">
      <circle r="340" fill="var(--red)"/><circle r="320" fill="var(--white)"/><circle r="88" fill="var(--red)"/></g></g></g>
    <g transform="translate(432 738) rotate(0)"><g class="segment" transform="translate(5 -8.5)"><g clip-path="url(#segment-clip)">
      <circle r="340" fill="var(--cyan)"/><circle r="320" fill="var(--white)"/><circle r="88" fill="var(--cyan)"/></g></g></g>
    <g transform="translate(432 738) rotate(60)"><g class="segment" transform="translate(5 -8.5)"><g clip-path="url(#segment-clip)">
      <circle r="340" fill="var(--green)"/><circle r="320" fill="var(--white)"/><circle r="88" fill="var(--green)"/></g></g></g>
    <g transform="translate(432 738) rotate(120)"><g class="segment" transform="translate(5 -8.5)"><g clip-path="url(#segment-clip)">
      <circle r="340" fill="var(--purple)"/><circle r="320" fill="var(--white)"/><circle r="88" fill="var(--purple)"/></g></g></g>
    <g transform="translate(432 738) rotate(180)"><g class="segment" transform="translate(5 -8.5)"><g clip-path="url(#segment-clip)">
      <circle r="340" fill="var(--yellow)"/><circle r="320" fill="var(--white)"/><circle r="88" fill="var(--yellow)"/></g></g></g>
    <g transform="translate(432 738) rotate(240)"><g class="segment" transform="translate(5 -8.5)"><g clip-path="url(#segment-clip)">
      <circle r="340" fill="var(--blue)"/><circle r="320" fill="var(--white)"/><circle r="88" fill="var(--blue)"/></g></g></g>
  </svg>

  <article class="value value--quality">
    <h3 class="value__title">QUALITY</h3>
    <p class="value__text">We strive for excellence through evidence<br>based practice,self-reflection, feedback and<br>a continuous commitment to improvement<br>and discovery both professionally and<br>personally.</p>
  </article>
  <article class="value value--flexibility">
    <h3 class="value__title">FLEXIBILITY</h3>
    <p class="value__text">We are flexible in our problem solving and<br>offer options and solutions for our families<br>and team wherever we reasonably can.</p>
  </article>
  <article class="value value--diversity">
    <h3 class="value__title">DIVERSITY</h3>
    <p class="value__text">We embed diversity by recognising,<br>respecting and appreciating<br>differences in our families<br>and our team.</p>
  </article>
  <article class="value value--positivity">
    <h3 class="value__title">POSITIVITY</h3>
    <p class="value__text">We lead ourselves ‘above the line’<br>choosing to adopt a positive,<br>accountable and solution-focused<br>mindset.</p>
  </article>
  <article class="value value--creativity">
    <h3 class="value__title">CREATIVITY</h3>
    <p class="value__text">We are innovative and collaborative,<br>constantly working towards new and<br>improved ways to support our clients,<br>families and our team.</p>
  </article>
  <article class="value value--integrity">
    <h3 class="value__title">INTEGRITY</h3>
    <p class="value__text">We care for and respect the needs and<br>well-being of our families, our team and<br>ourselves. We encourage openness, trust<br>and honest communication at all times.</p>
  </article>
</main>
</body>
</html>
```